Harlow Solutions Website

My business has been word of mouth over the last 3 years and has grown. Now I need a website for additional marketing as we have new clients asking for a website.

You have already completed my Logo during an earlier project. I have attached the logo.

We do Staff Augmentation and Operation Support.

What is that?
Staff augmentation is an outsourcing strategy that allows companies to fill specific, temporary roles to achieve business objectives. This staffing method complements existing teams with specific talent, enhancing business capabilities or filling gaps left by members on extended leave.

We work alongside the internal recruiting team to assist clients to meet and exceed financial goals.

```html
<!DOCTYPE html>
<html lang="en">
<head>
<meta charset="utf-8">
<title>Harlow Solutions</title>
<link href="https://fonts.googleapis.com/css2?family=Montserrat:wght@700;800&family=Poppins:ital,wght@0,400;0,500;0,600;1,400&family=Roboto+Condensed:wght@500;700&display=swap" rel="stylesheet">
<style>
:root{
  --blue:#0b5f99;
  --blue-dark:#084c7c;
  --blue-light:#d6e6f2;
  --ink:#1b1b1b;
  --muted:#6d6d6d;
  --grey:#efefef;
  --white:#ffffff;
  --black:#111111;
}
*{margin:0;padding:0;box-sizing:border-box}
html,body{width:1200px;height:4317px;overflow:hidden}
body{position:relative;font-family:"Poppins",sans-serif;color:var(--ink);background:var(--white)}
.abs{position:absolute}
.photo{position:absolute}
.cond{font-family:"Roboto Condensed",sans-serif}
p.body{font-size:11.5px;line-height:19px;color:var(--muted)}

/* header */
.hero-photo{left:340px;top:0;width:860px;height:637px;background:linear-gradient(120deg,#5c5850 0%,#8a8378 40%,#3c3a3a 70%,#b8b4ac 100%)}
.hero-shape{left:0;top:0}
.brand{display:flex;align-items:center;gap:10px;font-family:"Poppins",sans-serif;font-weight:600;font-size:20px;color:var(--blue)}
.brand .mark{width:34px;height:34px;border-radius:50%;background:var(--blue)}
.header-brand{left:130px;top:20px}
.nav{left:412px;top:28px;display:flex;font-size:11px;font-weight:500;color:var(--ink)}
.nav span{padding:0 13px}
.nav .active{color:var(--blue);background:#e6e6e6;border-radius:16px;padding:3px 9px;margin-top:-3px}
.auth{left:914px;top:15px;width:152px;height:38px;border:1.5px solid var(--blue);border-radius:20px;display:flex;font-size:11px;font-weight:600}
.auth span{flex:1;display:flex;align-items:center;justify-content:center}
.auth .login{background:var(--blue);color:var(--white);border-radius:20px}
.hero-title{left:62px;top:232px;font-family:"Montserrat",sans-serif;font-weight:800;font-size:49px;line-height:53px;color:var(--white);letter-spacing:.5px}
.hero-text{left:62px;top:412px;font-size:12px;line-height:22px;color:var(--white);width:380px}
.btn{display:flex;align-items:center;justify-content:center;border-radius:20px;font-size:12px;font-weight:600}
.btn-white{background:var(--white);color:var(--blue)}
.btn-blue{background:var(--blue);color:var(--white)}

/* section heading */
.h-sec{font-size:29px;font-weight:500;color:var(--ink);z-index:1}
.h-sec::before{content:"";position:absolute;left:-10px;top:2px;width:34px;height:34px;border-radius:50%;background:#e2e2e2;z-index:-1}

.frame{border:7px solid var(--white);box-shadow:0 2px 10px rgba(0,0,0,.18)}
.stat{display:flex;gap:12px;align-items:flex-start}
.stat b{font-family:"Poppins",sans-serif;font-size:27px;font-weight:600;display:block;line-height:30px}
.stat small{font-size:14px;color:var(--blue)}

.bullets{list-style:none}
.bullets li{position:relative;padding-left:30px;font-size:11.5px;line-height:19px;color:var(--muted);margin-bottom:15px;width:360px}
.bullets li::before{content:"";position:absolute;left:2px;top:4px;width:9px;height:9px;background:var(--blue);transform:rotate(45deg)}
.serv-title{font-family:"Poppins",sans-serif;font-size:20px;font-weight:500;white-space:nowrap}
.serv-title .num{color:var(--blue);margin-right:6px}

.news-card{position:absolute;top:3453px;width:286px;height:422px;background:var(--white);box-shadow:0 2px 10px rgba(0,0,0,.08)}
.news-card .img{height:210px;background:linear-gradient(135deg,#c9c4bc,#7b7570)}
.news-card .meta{position:absolute;left:75px;top:180px;width:211px;height:30px;background:var(--blue);color:var(--white);font-size:11px;display:flex;align-items:center;justify-content:center;gap:18px}
.news-card h4{font-family:"Roboto Condensed",sans-serif;font-size:15.5px;font-weight:700;line-height:24px;margin:18px 28px 0}
.news-card p{margin:18px 28px 0;font-size:11.5px;line-height:19px;color:var(--muted)}

.footer h5{font-family:"Roboto Condensed",sans-serif;font-size:20px;font-weight:700;color:var(--white)}
.footer ul{list-style:none;font-size:11.5px;color:var(--white);line-height:24px}
.ci{display:flex;gap:12px;align-items:center;color:var(--white);font-size:11.5px;line-height:18px;margin-bottom:18px}
.ci i{flex:none;width:30px;height:30px;border-radius:50%;border:1.5px solid var(--white);display:flex;align-items:center;justify-content:center}
.soc{width:32px;height:32px;border-radius:50%;border:1.5px solid var(--white)}
</style>
</head>
<body>

<!-- HERO -->
<div class="photo hero-photo" role="img" aria-label="Smiling businesswoman in a dark blazer in an office"></div>
<svg class="abs hero-shape" width="1200" height="670" viewBox="0 0 1200 670">
  <polygon points="0,0 680,0 362,665 0,665" fill="#0b5f99"/>
  <polygon points="0,0 680,0 480,430 0,430" fill="#0a6aa8" opacity=".55"/>
  <polygon points="60,0 1140,0 1100,78 100,78" fill="#ffffff"/>
  <polyline points="60,0 100,78 1100,78 1140,0" fill="none" stroke="#0b5f99" stroke-width="2"/>
</svg>
<div class="abs brand header-brand"><span class="mark"></span>Harlow Solutions</div>
<div class="abs nav"><span class="active">HOME</span><span>WHAT WE DO</span><span>SERVICES</span><span>WE WORK</span><span>NEWS</span><span>CONTACT US</span></div>
<div class="abs auth"><span class="login">LOGIN</span><span>REGISTER</span></div>
<h1 class="abs hero-title">Complements Existing<br>Teams With Specific<br>Talent</h1>
<p class="abs hero-text">Lorem Ipsum is simply dummy text of the printing and typesetting industry. Lorem Ipsum has been the industry's</p>
<div class="abs btn btn-white" style="left:60px;top:472px;width:135px;height:38px">CONTACT US</div>

<!-- WHAT IS THAT -->
<h2 class="abs h-sec" style="left:152px;top:737px">What is that?</h2>
<p class="abs cond" style="left:152px;top:792px;font-size:15px;font-weight:700;line-height:22px;color:var(--blue)">My business has been word of mouth over the<br>last 3 years and has grown.</p>
<p class="abs body" style="left:152px;top:840px;width:385px">Staff augmentation is an outsourcing strategy that allows companies to fill specific, temporary roles to achieve business objectives. This staffing method complements existing teams with specific talent, enhancing business capabilities or filling gaps left by members on extended leave.</p>
<div class="abs stat" style="left:150px;top:975px">
  <svg width="50" height="42" viewBox="0 0 50 42" fill="none" stroke="#0b5f99" stroke-width="2"><circle cx="25" cy="12" r="7"/><circle cx="10" cy="16" r="5"/><circle cx="40" cy="16" r="5"/><path d="M12 40c0-9 6-15 13-15s13 6 13 15zM2 36c0-6 4-10 8-10M48 36c0-6-4-10-8-10"/></svg>
  <div><b>105+</b><small>Team Members</small></div>
</div>
<div class="abs stat" style="left:358px;top:975px">
  <svg width="40" height="46" viewBox="0 0 40 46" fill="none" stroke="#0b5f99" stroke-width="2"><circle cx="20" cy="18" r="15" stroke-dasharray="4 3"/><circle cx="20" cy="18" r="9"/><path d="M20 13l1.6 3.4 3.6.4-2.7 2.4.8 3.6-3.3-1.9-3.3 1.9.8-3.6-2.7-2.4 3.6-.4z"/><path d="M12 31l-4 13 6-3 3 5 3-10M28 31l4 13-6-3-3 5-3-10"/></svg>
  <div><b>18+</b><small>Award Wining</small></div>
</div>
<div class="abs btn btn-blue" style="left:150px;top:1068px;width:127px;height:38px">LEARN MORE</div>
<div class="photo frame" style="left:720px;top:742px;width:268px;height:316px;background:linear-gradient(135deg,#b9b2a6,#6d6960)" role="img" aria-label="Team gathered around a laptop in a meeting room"></div>
<div class="photo frame" style="left:648px;top:948px;width:192px;height:174px;background:linear-gradient(135deg,#d7d1c8,#3d4a5a)" role="img" aria-label="Woman in a job interview across a table"></div>

<!-- WE DO -->
<div class="abs" style="left:0;top:1190px;width:1200px;height:989px;background:var(--grey)"></div>
<h2 class="abs h-sec" style="left:508px;top:1252px">We Do</h2>
<svg class="abs" style="left:130px;top:1310px" width="360" height="380" viewBox="0 0 360 380">
  <circle cx="300" cy="80" r="50" fill="none" stroke="#3f8fc6" stroke-width="5"/>
  <path d="M40 220 a130 130 0 0 0 110 130" fill="none" stroke="#bcd6ea" stroke-width="14"/>
  <circle cx="175" cy="180" r="162" fill="none" stroke="#0b5f99" stroke-width="2"/>
  <circle cx="175" cy="180" r="152" fill="#0b5f99"/>
</svg>
<div class="photo" style="left:168px;top:1352px;width:274px;height:274px;border-radius:50%;background:linear-gradient(135deg,#cfc9c0,#6a6460)" role="img" aria-label="Colleagues working together on laptops"></div>
<h3 class="abs serv-title" style="left:673px;top:1330px"><span class="num">01</span>Staff Augmentation</h3>
<p class="abs body" style="left:688px;top:1372px;width:370px">Lorem Ipsum is simply dummy text of the printing and typesetting industry. Lorem Ipsum has been the industry's standard dummy text ever since the 1500s</p>
<ul class="abs bullets" style="left:687px;top:1450px">
  <li>Lorem Ipsum is simply dummy text of the printing and typesetting industry.</li>
  <li>Lorem Ipsum is simply dummy text of the printing and typesetting industry.</li>
  <li>Lorem Ipsum is simply dummy text of the printing and typesetting industry.</li>
  <li>Lorem Ipsum is simply dummy text of the printing and typesetting industry.</li>
</ul>

<h3 class="abs serv-title" style="left:137px;top:1750px"><span class="num">02</span>Operation Support</h3>
<p class="abs body" style="left:152px;top:1792px;width:370px">Lorem Ipsum is simply dummy text of the printing and typesetting industry. Lorem Ipsum has been the industry's standard dummy text ever since the 1500s</p>
<ul class="abs bullets" style="left:150px;top:1870px">
  <li>Lorem Ipsum is simply dummy text of the printing and typesetting industry.</li>
  <li>Lorem Ipsum is simply dummy text of the printing and typesetting industry.</li>
  <li>Lorem Ipsum is simply dummy text of the printing and typesetting industry.</li>
  <li>Lorem Ipsum is simply dummy text of the printing and typesetting industry.</li>
</ul>
<svg class="abs" style="left:705px;top:1730px" width="360" height="380" viewBox="0 0 360 380">
  <circle cx="300" cy="80" r="50" fill="none" stroke="#3f8fc6" stroke-width="5"/>
  <path d="M40 220 a130 130 0 0 0 110 130" fill="none" stroke="#bcd6ea" stroke-width="14"/>
  <circle cx="175" cy="180" r="162" fill="none" stroke="#0b5f99" stroke-width="2"/>
  <circle cx="175" cy="180" r="152" fill="#0b5f99"/>
</svg>
<div class="photo" style="left:743px;top:1772px;width:274px;height:274px;border-radius:50%;background:linear-gradient(135deg,#d8d4cc,#5e5a58)" role="img" aria-label="Team meeting with laptops around a table"></div>

<!-- BLUE BAND -->
<div class="abs" style="left:0;top:2179px;width:1200px;height:226px;background:var(--blue)"></div>
<svg class="abs" style="left:0;top:2170px" width="1200" height="240" viewBox="0 0 1200 240">
  <circle cx="654" cy="14" r="11" fill="#2d79b0"/>
  <circle cx="0" cy="200" r="60" fill="#1a6ca6"/>
  <circle cx="6" cy="62" r="9" fill="none" stroke="#3f8fc6" stroke-width="2"/>
</svg>
<div class="photo" style="left:60px;top:2224px;width:300px;height:136px;background:linear-gradient(120deg,#dbe3ea,#4c5a68)" role="img" aria-label="Business team walking and talking in an office"></div>
<div class="abs" style="left:342px;top:2278px;width:36px;height:36px;background:var(--white);display:flex;align-items:center;justify-content:center">
  <svg width="18" height="18" viewBox="0 0 24 24" fill="#0b5f99"><path d="M6.6 10.8a15 15 0 0 0 6.6 6.6l2.2-2.2c.3-.3.7-.4 1-.2 1.1.4 2.3.6 3.6.6.6 0 1 .4 1 1V20c0 .6-.4 1-1 1A17 17 0 0 1 3 4c0-.6.4-1 1-1h3.5c.6 0 1 .4 1 1 0 1.3.2 2.5.6 3.6.1.3 0 .7-.2 1z"/></svg>
</div>
<h2 class="abs" style="left:462px;top:2248px;font-size:28px;font-weight:500;line-height:38px;color:var(--white)">This staffing method complements existing<br>teams with specific talent</h2>
<p class="abs" style="left:462px;top:2333px;font-size:14px;color:var(--white)">24/7 Service Available</p>

<!-- WE DO? -->
<h2 class="abs h-sec" style="left:148px;top:2478px">We Do?</h2>
<p class="abs body" style="left:148px;top:2540px;width:360px">Lorem Ipsum is simply dummy text of the printing and typesetting industry. Lorem Ipsum has been the industry's standard dummy text ever since the 1500s</p>
<div class="abs" style="left:146px;top:2618px;width:70px;height:70px;border-radius:50%;border:2px solid var(--blue-light);display:flex;align-items:center;justify-content:center">
  <svg width="40" height="34" viewBox="0 0 40 34" fill="none" stroke="#0b5f99" stroke-width="1.8"><circle cx="20" cy="8" r="5"/><circle cx="7" cy="12" r="4"/><circle cx="33" cy="12" r="4"/><path d="M11 32c0-8 4-13 9-13s9 5 9 13zM1 30c0-5 3-9 6-9M39 30c0-5-3-9-6-9"/></svg>
</div>
<h4 class="abs cond" style="left:241px;top:2620px;font-size:16px;font-weight:700;color:var(--blue)">Internal recruiting team</h4>
<p class="abs body" style="left:241px;top:2645px;width:270px">Lorem Ipsum is simply dummy text of the printing and typesetting industry.</p>
<div class="abs" style="left:146px;top:2708px;width:70px;height:70px;border-radius:50%;border:2px solid var(--blue-light);display:flex;align-items:center;justify-content:center">
  <svg width="38" height="36" viewBox="0 0 38 36" fill="none" stroke="#0b5f99" stroke-width="1.8"><rect x="3" y="4" width="32" height="24"/><path d="M8 22l7-7 5 4 9-9M19 28v6M12 34h14"/></svg>
</div>
<h4 class="abs cond" style="left:241px;top:2711px;font-size:16px;font-weight:700;color:var(--blue)">Meet and exceed financial goals.</h4>
<p class="abs body" style="left:241px;top:2736px;width:270px">Lorem Ipsum is simply dummy text of the printing and typesetting industry.</p>
<div class="photo" style="left:637px;top:2478px;width:251px;height:277px;background:linear-gradient(135deg,#6d4f38,#3e2c20)" role="img" aria-label="Overhead view of a team meeting at a wooden table"></div>
<div class="photo" style="left:905px;top:2510px;width:120px;height:160px;background:linear-gradient(135deg,#5d7fa8,#2a3a52)" role="img" aria-label="Two colleagues reviewing a document"></div>
<div class="photo" style="left:825px;top:2690px;width:143px;height:98px;background:linear-gradient(135deg,#d9d4cc,#6f6a66)" role="img" aria-label="Business team in discussion"></div>

<!-- TESTIMONIALS -->
<div class="abs" style="left:188px;top:2862px;width:1012px;height:448px;background:#e6e6e6"></div>
<svg class="abs" style="left:0;top:3040px" width="150" height="450" viewBox="0 0 150 450">
  <path d="M0 20 a200 200 0 0 1 0 400" fill="none" stroke="#0b5f99" stroke-width="12" opacity=".85"/>
</svg>
<div class="photo" style="left:60px;top:2906px;width:288px;height:337px;background:linear-gradient(135deg,#6b5646,#2f2620)" role="img" aria-label="Smiling woman holding a tablet at a desk"></div>
<h2 class="abs h-sec" style="left:500px;top:2948px">Testimonials</h2>
<p class="abs cond" style="left:500px;top:2990px;font-size:15px;font-weight:700;color:var(--blue)">What Our Client Say</p>
<div class="abs" style="left:498px;top:3018px;font-family:'Montserrat',sans-serif;font-size:48px;font-weight:800;color:var(--blue);line-height:48px">&ldquo;</div>
<p class="abs" style="left:500px;top:3075px;width:520px;font-size:13px;font-style:italic;line-height:21px;color:var(--ink)">Lorem Ipsum is simply dummy text of the printing and typesetting industry. Lorem Ipsum has been the industry's standard dummy text ever since the 1500s,when an unknown printer took a galley of type and scrambled it to make a type specimen book.</p>
<p class="abs" style="left:500px;top:3182px;font-size:20px;font-weight:500;color:var(--blue)">Maren Holt</p>
<p class="abs" style="left:500px;top:3212px;font-size:12px">Operation Support</p>
<div class="abs" style="left:1008px;top:3204px;width:33px;height:33px;background:var(--blue);display:flex;align-items:center;justify-content:center">
  <svg width="14" height="14" viewBox="0 0 14 14"><path d="M9 2L4 7l5 5" fill="none" stroke="#fff" stroke-width="2"/></svg></div>
<div class="abs" style="left:1052px;top:3204px;width:33px;height:33px;background:var(--white);display:flex;align-items:center;justify-content:center">
  <svg width="14" height="14" viewBox="0 0 14 14"><path d="M5 2l5 5-5 5" fill="none" stroke="#0b5f99" stroke-width="2"/></svg></div>

<!-- NEWS -->
<h2 class="abs h-sec" style="left:518px;top:3388px">News</h2>
<div class="news-card" style="left:138px">
  <div class="img" role="img" aria-label="Job candidates waiting in a row with laptops"></div>
  <div class="meta"><span>11 jan 2022</span><span>/</span><span>Branding</span></div>
  <h4>My business has been word of mouth over the last 3 years and has grown.</h4>
  <p>Lorem Ipsum is simply dummy text of the printing and typesetting industry. Lorem Ipsum has been the industry's</p>
</div>
<div class="news-card" style="left:453px">
  <div class="img" role="img" aria-label="Colleagues smiling around a laptop"></div>
  <div class="meta"><span>11 jan 2022</span><span>/</span><span>Branding</span></div>
  <h4>My business has been word of mouth over the last 3 years and has grown.</h4>
  <p>Lorem Ipsum is simply dummy text of the printing and typesetting industry. Lorem Ipsum has been the industry's</p>
</div>
<div class="news-card" style="left:768px">
  <div class="img" role="img" aria-label="Team meeting in a bright modern office"></div>
  <div class="meta"><span>11 jan 2022</span><span>/</span><span>Branding</span></div>
  <h4>My business has been word of mouth over the last 3 years and has grown.</h4>
  <p>Lorem Ipsum is simply dummy text of the printing and typesetting industry. Lorem Ipsum has been the industry's</p>
</div>

<!-- FOOTER -->
<footer class="footer">
  <div class="abs" style="left:0;top:3947px;width:1200px;height:335px;background:var(--blue)"></div>
  <div class="abs brand" style="left:60px;top:4032px;color:var(--white)"><span class="mark" style="background:var(--white)"></span>Harlow Solutions</div>
  <div class="abs" style="left:60px;top:4104px;display:flex;gap:6px"><span class="soc"></span><span class="soc"></span><span class="soc"></span></div>

  <h5 class="abs" style="left:337px;top:4010px">Site Map</h5>
  <ul class="abs" style="left:337px;top:4050px">
    <li>- Home</li><li>- About Us</li><li>- Services</li><li>- we Work</li><li>- Testimonials</li><li>- Blog</li><li>- Contact Us</li>
  </ul>

  <h5 class="abs" style="left:612px;top:4010px">Contact Us</h5>
  <div class="abs" style="left:610px;top:4050px;width:230px">
    <div class="ci"><i><svg width="12" height="14" viewBox="0 0 12 14" fill="#fff"><path d="M6 0a5 5 0 0 0-5 5c0 4 5 9 5 9s5-5 5-9a5 5 0 0 0-5-5zm0 7a2 2 0 1 1 0-4 2 2 0 0 1 0 4z"/></svg></i><span>101 - Lorem ipum is dummy printing text</span></div>
    <div class="ci"><i><svg width="13" height="13" viewBox="0 0 24 24" fill="#fff"><path d="M6.6 10.8a15 15 0 0 0 6.6 6.6l2.2-2.2c.3-.3.7-.4 1-.2 1.1.4 2.3.6 3.6.6.6 0 1 .4 1 1V20c0 .6-.4 1-1 1A17 17 0 0 1 3 4c0-.6.4-1 1-1h3.5c.6 0 1 .4 1 1 0 1.3.2 2.5.6 3.6.1.3 0 .7-.2 1z"/></svg></i><span>+1 555 010 2040</span></div>
    <div class="ci"><i><svg width="13" height="10" viewBox="0 0 13 10" fill="#fff"><path d="M0 0h13v10H0zM1 1.2v.4l5.5 3.8L12 1.6v-.4z" fill-rule="evenodd"/></svg></i><span>info@harlowsolutions.com</span></div>
  </div>

  <h5 class="abs" style="left:888px;top:4010px">News Letter</h5>
  <div class="abs" style="left:888px;top:4052px;width:300px;height:36px;border-radius:20px;background:var(--white);font-size:11px;color:#888;display:flex;align-items:center;padding-left:16px">Enter Email Address...</div>
  <div class="abs btn btn-white" style="left:888px;top:4110px;width:128px;height:36px">SUBSRIBE</div>

  <div class="abs" style="left:0;top:4282px;width:1200px;height:35px;background:var(--black);color:var(--white);font-size:11px;display:flex;align-items:center;justify-content:center">Copy Right © 2022 - All Right Reserved.</div>
</footer>

</body>
</html>
```